Contest - label design for a health related product with 4 color variations

Nuvera-Store (http://www.nuvera-store.example) is an online shop selling health related products and nutritional supplements, such as algae products, wheat grass and barley grass powder. These products have a positive impact on a person's health. Through Craft Hive, we have designed already a logo for the shop and now we need to create labels that will be placed on a brown glass bottle (see attachment). The logo shall be used without the slogan 'One life. Live it healthy.' when creating the label.

Your job is to design a label with 4 color variations, blue, green, red and yellow. The measurements of the label is 80 mm x 173 mm, but please add 3 mm bleed to each side.

The information that has to go on the label can be taken from the attachment 'label information.pdf'. For the sake of communication, we will divide the label into 3 parts

- left
- middle
- right

The left part and the right part are fixed as this contains legal information. Please use easy to read fonts, non-serifed fonts, such as Arial, Verdana, Calibri. The left part contains a table and if Illustrator provides the possibility for tables, please use it as we need to be able to easily add and remove rows of the table.

The middle part contains the product description, the product quantity (i.e. 100 g), our logo without the slogan 'One live. Live it healthy.' and logos indicating the organic quality of the product (please see attachments). For the product name (i.e. KEM-Tangen) and the quantity (i.e. 100 Tabletten, 200 g) use the attached Lato font. Please note that the vertical position of our logo, the product name and the organic logos has NOT been set yet. You are free to position them where ever you feel in the middle part of the label.

Target Market(s)

Health concious people between 25 and 70

Industry/Entity Type

Health

Requirements
Must have
• - the attached logo without the slogan "One life...."
- the following attributes: healthy, joyful, vivid, lively, abstract, minimalistic
- colors that go along with our logo and the website www.nuvera-store.example
- all fonts need to be editable and not rendered
- the left part should have an editable table where we can add rows if necessary
- the attached font for product name and quantity
- 3 mm bleed on each side, so the final design is 6 mm wider and higher
- the final design will be in editable Illustrator files of a recent version.
Should not have
• - many overlaying, confusing lines or layers
- dark colors
- heavy appearance

```html
<!DOCTYPE html>
<html lang="de">
<head>
<meta charset="utf-8">
<title>KEM-Tangen – Etikett</title>
<link href="https://fonts.googleapis.com/css2?family=Lato:wght@400;700;900&family=Open+Sans:wght@400;600&display=swap" rel="stylesheet">
<style>
  :root{
    --green:#13a35a;
    --green-dark:#0e8a4b;
    --orange:#f3a529;
    --swirl-light:#fbe6c2;
    --swirl-mid:#f2c98a;
    --paper:#ffffff;
    --ink:#2b2b2b;
    --eu-green:#8dc63f;
  }
  *{box-sizing:border-box;margin:0;padding:0}
  html,body{width:1200px;height:1000px;overflow:hidden;background:#fff}
  body{font-family:"Open Sans",Arial,sans-serif;color:var(--ink);position:relative}

  .label{position:absolute;left:60px;top:250px;width:1080px;height:500px;background:var(--green);overflow:hidden}
  .label__shapes{position:absolute;inset:0}

  /* left legal part */
  .legal-left{position:absolute;left:22px;top:40px;width:300px;height:400px;background:var(--paper);padding:14px 16px;font-size:10px;line-height:1.35}
  .legal-left__intro{margin-bottom:10px}
  .nutrition{width:100%;border-collapse:collapse;margin-bottom:10px;border:1px solid var(--green)}
  .nutrition th{background:var(--green);color:#fff;font-weight:600;text-align:left;padding:3px 6px;font-size:9.5px}
  .nutrition th.num,.nutrition td.num{text-align:right}
  .nutrition td{padding:3px 6px;border-top:1px solid #d9eee2}
  .legal-left__note{font-size:9.5px}
  .shop-url{position:absolute;left:34px;top:470px;color:#fff;font-weight:600;font-size:13px}

  /* middle part */
  .brand{position:absolute;left:470px;top:58px;width:300px;text-align:center}
  .brand__name{display:inline-flex;align-items:center;gap:8px;font-weight:600;font-size:20px;color:var(--green)}
  .brand__dot{width:12px;height:12px;border-radius:50%;background:var(--orange)}
  .swirl{position:absolute;left:505px;top:120px;width:290px;height:290px;border-radius:50%;
    background:radial-gradient(circle at 50% 50%,var(--swirl-light) 0%,var(--swirl-mid) 65%,rgba(242,201,138,0) 100%)}
  .product-name{position:absolute;left:470px;top:180px;width:330px;text-align:center;font-family:"Lato",Arial,sans-serif;font-weight:900;font-size:40px;color:var(--green-dark);letter-spacing:.3px}
  .badges{position:absolute;left:510px;top:334px;display:flex;gap:24px;align-items:center}
  .badge-eu{width:64px;height:42px;background:var(--eu-green)}
  .badge-hex{width:50px;height:46px;background:var(--paper);clip-path:polygon(25% 0,75% 0,100% 50%,75% 100%,25% 100%,0 50%)}

  /* right legal part */
  .legal-right{position:absolute;left:842px;top:60px;width:210px;color:#fff;font-size:11px;line-height:1.5}
  .legal-right p{margin-bottom:12px}
  .legal-right__qty{font-family:"Lato",Arial,sans-serif;font-weight:700;font-size:16px}
</style>
</head>
<body>
  <section class="label" aria-label="Etikett KEM-Tangen">
    <svg class="label__shapes" width="1080" height="500" viewBox="0 0 1080 500">
      <rect class="band-top" x="0" y="0" width="1080" height="20" fill="var(--orange)"/>
      <rect class="band-bottom" x="0" y="446" width="1080" height="20" fill="var(--orange)"/>
      <path class="middle-edge" d="M340 32 H770 C800 120 812 300 790 420 Q780 450 740 452 H340 Z" fill="var(--orange)"/>
      <path class="middle-panel" d="M340 32 H740 C770 120 780 300 760 404 Q750 432 712 434 H340 Z" fill="var(--paper)"/>
    </svg>

    <div class="legal-left">
      <p class="legal-left__intro">Bio-Algenkapseln aus reinem Bergsee, schonend getrocknet.</p>
      <table class="nutrition">
        <tr><th>Nährwerte</th><th class="num">pro Kapsel</th></tr>
        <tr><td>Algenpulver</td><td class="num">400 mg</td></tr>
        <tr><td>Eiweiß</td><td class="num">240 mg</td></tr>
        <tr><td>Vitamin B12</td><td class="num">1,25 µg</td></tr>
      </table>
      <table class="nutrition">
        <tr><th></th><th class="num">% RDA</th></tr>
        <tr><td>Vitamin B12</td><td class="num">50%</td></tr>
      </table>
      <p class="legal-left__note">Kühl und trocken lagern. Außerhalb der Reichweite von Kindern.</p>
    </div>
    <p class="shop-url">www.nuvera-store.example</p>

    <div class="brand">
      <span class="brand__name"><span class="brand__dot"></span>Nuvera-Store</span>
    </div>
    <div class="swirl" role="img" aria-label="Abstrakte orange Pinselspirale als Hintergrunddekor"></div>
    <h1 class="product-name">KEM-Tangen</h1>
    <div class="badges">
      <div class="badge-eu" role="img" aria-label="Bio-Siegel"></div>
      <div class="badge-hex" role="img" aria-label="Bio-Prüfzeichen"></div>
    </div>

    <div class="legal-right">
      <p>Verzehrempfehlung: täglich 2 Kapseln mit Wasser einnehmen.</p>
      <p>Kein Ersatz für eine ausgewogene Ernährung.</p>
      <p class="legal-right__qty">Inhalt: 100 Kapseln</p>
      <p>Kontrollstelle: DE-ÖKO-000</p>
    </div>
  </section>
</body>
</html>
```